Current website re-design to a updated look and feel.

We currently have a website www.brightlanefreight.com that we want to give an updated look and feel to. We are a logistics company that competes with Falcora, Dw Hartley, Vanta but on a smaller scale. We want something fresh and updated. We have two locations one in downtown Chicago, IL and one in Palatine IL. We are a fun group that also gets the job done. We know we need pictures of both locations and possibly a video, but we need fresh design ideas. The 'who we are' page is really the only page that we currently want to keep. The 'what we do' page needs to be completely re-done from a look and feel for sure.

Target Market(s)

Anyone who uses Truck transportation to move their product. Mainly US manufacturers.

Industry/Entity Type

Logistics

Number of Pages Required

5+ page

Font styles to use
Sans Serif

Colors
5c91c4
0355a3
d0dfed

Requirements
Must have
• The new design must entice people to want to do business with us. The design must have locations for pictures and at least one video which we know we will have to provide. Design must be easy to navigate.

```html
<!DOCTYPE html>
<html lang="en">
<head>
<meta charset="utf-8">
<title>Brightlane Freight – Home</title>
<link href="https://fonts.googleapis.com/css2?family=Titillium+Web:wght@400;600;700&family=Open+Sans:wght@400;600;700&display=swap" rel="stylesheet">
<style>
  :root{
    --brand:#0355a3;
    --brand-mid:#5c91c4;
    --brand-pale:#d0dfed;
    --accent:#29a8e0;
    --nav-active:#e0262f;
    --ink:#1d1d1d;
    --body:#7a7a7a;
    --muted:#9a9a9a;
    --band:#ececec;
    --white:#ffffff;
  }
  *{box-sizing:border-box;margin:0;padding:0}
  html,body{width:1200px;height:1200px;overflow:hidden;background:var(--white)}
  body{position:relative;font-family:"Open Sans",Arial,sans-serif;color:var(--ink)}
  .abs{position:absolute}

  /* header */
  .brand{left:232px;top:50px;display:flex;align-items:center;gap:6px}
  .brand-name{font-family:"Open Sans",sans-serif;font-weight:400;font-size:30px;color:var(--brand);letter-spacing:-0.5px}
  .brand-tag{font-size:6px;line-height:7px;font-weight:700;color:var(--brand);margin-top:4px}
  .contact{top:55px;display:flex;flex-direction:column;gap:6px}
  .contact-label{display:flex;align-items:center;gap:4px;font-size:7.5px;color:var(--muted)}
  .contact-value{font-size:8.5px;color:#333}
  .divider{top:54px;width:1px;height:28px;background:#ddd}

  /* nav */
  .nav-strip{left:149px;top:116px;width:902px;height:18px;background:var(--brand)}
  .nav{left:408px;top:97px;width:643px;height:37px;background:var(--brand);clip-path:polygon(20px 0,100% 0,100% 100%,0 100%)}
  .nav ul{list-style:none;display:flex;position:absolute;left:37px;top:0;height:37px;align-items:center;gap:0}
  .nav li{font-size:8.5px;font-weight:600;color:var(--white);margin-right:29px;position:relative;height:37px;line-height:37px}
  .nav li.active::after{content:"";position:absolute;left:-4px;right:-8px;bottom:0;height:2px;background:var(--nav-active)}
  .social{right:24px;top:13px;display:flex;gap:7px;align-items:center}
  .social .sep{width:1px;height:9px;background:var(--brand-pale);margin-right:8px}
  .social span.dot{width:7px;height:7px;border-radius:50%;background:var(--white)}

  /* hero */
  .hero{left:149px;top:134px;width:902px;height:355px;
    background:linear-gradient(180deg,#3d4a5c 0%,#6b7888 30%,#5a5d66 55%,#4a3f3c 100%)}
  .hero-panel{left:246px;top:199px;width:348px;height:245px;background:rgba(18,92,170,.72)}
  .rule{width:32px;height:2px;background:var(--accent)}
  .hero-panel .rule{position:absolute;left:30px;top:43px}
  .hero-title{position:absolute;left:30px;top:60px;font-family:"Titillium Web",sans-serif;font-weight:600;font-size:33px;line-height:39px;color:var(--white)}
  .hero-text{position:absolute;left:30px;top:150px;font-size:9px;font-weight:600;line-height:18.5px;color:var(--white)}

  /* welcome */
  .network{left:149px;top:489px;width:330px;height:110px;
    background:radial-gradient(ellipse at 30% 30%,rgba(200,208,218,.35),rgba(255,255,255,0) 70%)}
  .welcome .rule{position:absolute;left:246px;top:535px}
  .welcome-title{left:245px;top:553px;font-family:"Titillium Web",sans-serif;font-weight:400;font-size:23px;color:var(--brand)}
  .welcome-text{left:246px;top:598px;width:350px;font-size:8.6px;line-height:16.8px;color:var(--body)}
  .signature{left:246px;top:764px;font-size:10px;font-weight:600;color:var(--ink)}
  .video{left:613px;top:536px;width:348px;height:230px;
    background:linear-gradient(135deg,#7a5e4a 0%,#b89a80 35%,#d8d2c8 60%,#6d8aa4 100%)}
  .play{left:760px;top:624px;width:54px;height:54px}

  /* services */
  .services{left:149px;top:817px;width:902px;height:360px;background:var(--band)}
  .services .rule{position:absolute;left:246px;top:867px}
  .services-title{left:245px;top:890px;font-family:"Titillium Web",sans-serif;font-weight:400;font-size:23px;line-height:31px;color:var(--brand)}
  .services-text{left:246px;top:967px;width:165px;font-size:8.6px;line-height:16.8px;color:var(--body)}
  .pager{left:246px;top:1082px;display:flex;gap:9px;align-items:center}
  .pager .ring{width:6px;height:6px;border:1px solid var(--brand);border-radius:50%}
  .pager .pip{width:3px;height:3px;background:var(--brand);border-radius:50%}
  .card{top:867px;width:165px;height:259px;background:var(--white)}
  .card-photo{height:110px}
  .card h3{position:absolute;left:19px;top:129px;font-size:8.5px;font-weight:700;color:var(--brand);letter-spacing:.2px}
  .card p{position:absolute;left:19px;top:151px;width:130px;font-size:8.6px;line-height:15px;color:var(--body)}
  .card .more{position:absolute;left:19px;top:228px;font-size:9px;color:var(--brand);display:flex;align-items:center;gap:5px}

  .footer-photo{left:604px;top:1177px;width:447px;height:23px;
    background:linear-gradient(90deg,#5a7290,#8aa0b8 60%,#6e849e);clip-path:polygon(0 0,100% 0,100% 100%,10px 100%)}
</style>
</head>
<body>

<header>
  <div class="abs brand">
    <span class="brand-name">Brightlane</span>
    <span class="brand-tag">Transportation<br>Distribution &amp;<br>Warehousing Inc.</span>
  </div>

  <div class="abs contact" style="left:618px">
    <span class="contact-label">
      <svg width="9" height="9" viewBox="0 0 10 10"><path d="M2 6V5a3 3 0 0 1 6 0v1" fill="none" stroke="#333" stroke-width="1.2"/><rect x="1" y="5.5" width="2" height="3" fill="#333"/><rect x="7" y="5.5" width="2" height="3" fill="#333"/></svg>
      Call Us Anytime</span>
    <span class="contact-value">312.555.0148</span>
  </div>
  <div class="abs divider" style="left:710px"></div>
  <div class="abs contact" style="left:729px">
    <span class="contact-label">
      <svg width="9" height="9" viewBox="0 0 10 10"><circle cx="5" cy="5" r="4" fill="none" stroke="#333" stroke-width="1.1"/><path d="M5 2.5V5h2" fill="none" stroke="#333" stroke-width="1.1"/></svg>
      Opening Time</span>
    <span class="contact-value">08:00 - 18:00</span>
  </div>
  <div class="abs divider" style="left:813px"></div>
  <div class="abs contact" style="left:832px">
    <span class="contact-label">
      <svg width="10" height="8" viewBox="0 0 10 8"><rect x=".5" y=".5" width="9" height="7" fill="none" stroke="#333"/><path d="M.5 .5 5 4.5 9.5 .5" fill="none" stroke="#333"/></svg>
      Email Us</span>
    <span class="contact-value">Rates@brightlanefreight.com</span>
  </div>

  <div class="abs nav-strip"></div>
  <nav class="abs nav">
    <ul>
      <li class="active">Home</li>
      <li>What We Do</li>
      <li>How We Do It</li>
      <li>Who We Are</li>
      <li>Tracking</li>
      <li>Chat</li>
      <li>Contact</li>
    </ul>
    <div class="abs social"><span class="sep"></span><span class="dot"></span><span class="dot"></span><span class="dot"></span><span class="dot"></span></div>
  </nav>
</header>

<section class="hero-section">
  <div class="abs hero" role="img" aria-label="Container port with stacked shipping containers and cranes under a cloudy sky"></div>
  <div class="abs hero-panel">
    <div class="rule"></div>
    <h1 class="hero-title">SEA &amp; OCEAN<br>DELIVERY</h1>
    <p class="hero-text">Lorem Ipsum is simply dummy text of<br>the printing and typesetting industry.<br>Lorem Ipsum has been the.</p>
  </div>
</section>

<section class="welcome">
  <div class="abs network"></div>
  <div class="rule"></div>
  <h2 class="abs welcome-title">WELCOME FROM OUR FOUNDER</h2>
  <p class="abs welcome-text">Brightlane Freight welcomes you to our growing family of clients! We have over 26 years of experience in helping people solve their logistics needs from coast-to-coast. We also provide friendly, exceptional service that makes it easy to do business with us. Give us a call today and experience the difference for your­self!<br>"Our service commitment begins from the moment you contact us. We appreciate your trust, and we go the extra mile to ensure that your freight is handled with care and expediency. If an issue comes up, we work tirelessly to resolve it, staying in contact with you until your freight is delivered without issue!"</p>
  <p class="abs signature">Dana Whitfield, Founder</p>
  <div class="abs video" role="img" aria-label="Video still of the team meeting around an office table"></div>
  <svg class="abs play" viewBox="0 0 54 54"><circle cx="27" cy="27" r="25" fill="rgba(3,85,163,.75)" stroke="#fff" stroke-width="2.5"/><path d="M22 18v18l14-9z" fill="#fff"/></svg>
</section>

<section>
  <div class="abs services"></div>
  <div class="rule"></div>
  <h2 class="abs services-title">SPECLAL<br>SERVICES</h2>
  <p class="abs services-text">There are many variations of passag­es of Lorem Ipsum available, but the majority have suffered alteration in some form, by injected humour, or randomised words which don't look even slightly believable.</p>
  <div class="abs pager"><span class="ring"></span><span class="pip"></span></div>

  <article class="abs card" style="left:429px">
    <div class="card-photo" role="img" aria-label="Container terminal at dusk" style="background:linear-gradient(180deg,#3a5a86 0%,#7d93ad 45%,#6a5a50 100%)"></div>
    <h3>FREIGHT MANAGEMENT</h3>
    <p>We strive for a perfect deliv­ery and promise to be there for anything you may need, every step of the way.</p>
    <span class="more">read more <svg width="11" height="6" viewBox="0 0 11 6"><path d="M0 3h10M7 .5 10 3 7 5.5" fill="none" stroke="#0355a3"/></svg></span>
  </article>

  <article class="abs card" style="left:613px">
    <div class="card-photo" role="img" aria-label="Highway with light trails at sunset" style="background:linear-gradient(180deg,#8a8a96 0%,#b89a86 25%,#4c5666 55%,#2f3845 100%)"></div>
    <h3>TRANSPORTATION</h3>
    <p>With a combined 500+ years of industry experience between all employees, we are the logistics...</p>
    <span class="more">read more <svg width="11" height="6" viewBox="0 0 11 6"><path d="M0 3h10M7 .5 10 3 7 5.5" fill="none" stroke="#0355a3"/></svg></span>
  </article>

  <article class="abs card" style="left:797px">
    <div class="card-photo" role="img" aria-label="Red semi truck pulling a trailer on the road" style="background:linear-gradient(180deg,#4a7fc0 0%,#a9c3de 45%,#b83a3a 70%,#5e5e5e 100%)"></div>
    <h3>CARRIERS</h3>
    <p>Are you a carrier looking to work with Brightlane? Click here to find out why we have the best carrier...</p>
    <span class="more">read more <svg width="11" height="6" viewBox="0 0 11 6"><path d="M0 3h10M7 .5 10 3 7 5.5" fill="none" stroke="#0355a3"/></svg></span>
  </article>
</section>

<div class="abs footer-photo" role="img" aria-label="Sky and landscape banner"></div>

</body>
</html>
```